Business Card and Letterhead Design for Public Accounting Firm

Business card and letterhead design for a CPA Firm located in Orange County, CA. We're looking for a modern and professional design utilizing our existing logo. We'd like a clean "less is more" look, but also something that catches the eye. We provide a high level of service to our clients. Open to single or double sided business cards.

Additional info: color numbers on logo
Blue :
R 0
G 83
B 125

#00537D

Silver :

R 154
G 154
B 154

#9A9A9A

Target Market(s)

Businesses and individuals

Industry/Entity Type

Accounting

Contact Information for Business Card

Moss Whitfield & Danby LLP - 4827 Larkspur Vale Road, Irvine, CA 92614 - (949)731-2864 - mwdaccts.example

Font styles to use
Serif
Sans Serif
Other font styles liked:
• See font file uploaded

Colors
0054AA
0677BA
7BADD7
CADEEF
E8F1F8

Requirements
Nice to have
• Possibly use the font file provided which matches our logo, but adjust to be not in all caps

```html
<!DOCTYPE html>
<html lang="en">
<head>
<meta charset="utf-8">
<title>Moss Whitfield &amp; Danby LLP — Stationery</title>
<link href="https://fonts.googleapis.com/css2?family=Cinzel:wght@400&family=Open+Sans:ital,wght@0,400;0,600;0,700;1,400&display=swap" rel="stylesheet">
<style>
  :root {
    --brand-blue: #0a5580;
    --brand-blue-dark: #084a70;
    --silver: #9a9a9a;
    --ink: #55595e;
    --paper: #ffffff;
    --backdrop: #e4e7e8;
    --watermark: #f1f2f3;
    --rule: #c9cdd1;
  }
  * { box-sizing: border-box; margin: 0; padding: 0; }
  html, body { width: 1200px; height: 900px; overflow: hidden; }
  body {
    background: var(--backdrop);
    font-family: "Open Sans", Arial, sans-serif;
    color: var(--ink);
    position: relative;
  }
  .sheet { position: absolute; background: var(--paper); box-shadow: 0 6px 18px rgba(0,0,0,.12); overflow: hidden; }

  .firm-name {
    font-family: "Cinzel", Georgia, serif;
    font-weight: 400;
    color: var(--brand-blue);
    letter-spacing: .08em;
    line-height: 1.15;
    display: flex; align-items: center; gap: 8px;
  }
  .firm-name .mark-square { width: 10px; height: 10px; background: var(--brand-blue); flex: none; }

  .accent-stripe { position: absolute; left: 0; bottom: 0; width: 100%; height: 12px; }

  .watermark {
    position: absolute;
    font-family: "Cinzel", Georgia, serif;
    color: var(--watermark);
    white-space: nowrap;
    line-height: 1;
  }

  .icon-line { display: flex; align-items: center; gap: 5px; }
  .icon-line svg { width: 8px; height: 8px; flex: none; fill: var(--brand-blue); }

  /* Letterhead */
  .letterhead { left: 40px; top: 50px; width: 460px; height: 595px; }
  .letterhead .firm-name { position: absolute; left: 36px; top: 40px; font-size: 14px; width: 200px; }
  .letterhead .contact-block {
    position: absolute; right: 34px; top: 92px; font-size: 7px; line-height: 1.45; display: flex; gap: 14px;
  }
  .letterhead .letter-body { position: absolute; left: 36px; top: 150px; width: 388px; font-size: 8.2px; line-height: 1.55; }
  .letter-body p { margin-bottom: 9px; }
  .signature-area { width: 70px; height: 28px; background: #eef1f4; margin-top: 6px; }
  .letterhead .watermark { right: 24px; bottom: 26px; font-size: 40px; }

  /* Folder */
  .folder { left: 540px; top: 50px; width: 300px; height: 390px; background: linear-gradient(135deg, #0c5a86, var(--brand-blue-dark)); }
  .folder .firm-name { color: #fff; position: absolute; left: 30px; right: 30px; top: 140px; font-size: 28px; justify-content: center; text-align: center; }
  .folder .folder-url { position: absolute; left: 0; right: 0; bottom: 34px; text-align: center; color: #fff; font-size: 13px; letter-spacing: .04em; }

  /* Business cards */
  .card { width: 290px; height: 166px; left: 870px; }
  .card-front { top: 50px; }
  .card-front .holder-name { position: absolute; left: 18px; top: 24px; font-size: 10px; font-weight: 700; color: var(--brand-blue); letter-spacing: .02em; white-space: nowrap; }
  .card-front .holder-title { position: absolute; left: 18px; top: 39px; font-size: 7.5px; font-style: italic; }
  .card-front .contact-list { position: absolute; left: 18px; top: 58px; font-size: 7.5px; line-height: 1.6; }
  .card-front .firm-name { position: absolute; right: 14px; top: 20px; font-size: 8.5px; width: 112px; letter-spacing: .06em; }
  .card-front .rule { position: absolute; left: 130px; right: 18px; top: 100px; height: 1px; background: var(--rule); }
  .card-front .address { position: absolute; right: 18px; top: 108px; font-size: 7.5px; text-align: right; line-height: 1.5; font-style: italic; }
  .card-back { top: 236px; background: linear-gradient(135deg, var(--brand-blue-dark), #0c5a86); }
  .card-back .firm-name { position: absolute; left: 30px; right: 30px; top: 66px; font-size: 15px; color: #dfe8ef; justify-content: center; }

  /* Envelope */
  .envelope { left: 540px; top: 470px; width: 620px; height: 272px; }
  .envelope .firm-name { position: absolute; left: 30px; top: 28px; font-size: 15px; width: 230px; }
  .envelope .return-address { position: absolute; left: 30px; top: 150px; font-size: 9.5px; line-height: 1.5; }
  .envelope .watermark { right: 36px; bottom: 34px; font-size: 46px; }
</style>
</head>
<body>

  <!-- Letterhead -->
  <section class="sheet letterhead">
    <div class="firm-name"><span class="mark-square"></span>Moss Whitfield &amp; Danby LLP</div>
    <div class="contact-block">
      <div>Moss Whitfield &amp; Danby LLP<br>4827 Larkspur Vale Road,<br>Irvine, CA 92614</div>
      <div>
        <div class="icon-line"><svg viewBox="0 0 10 10"><path d="M2 0h2l1 3-1.5 1a6 6 0 0 0 2.5 2.5L7 5l3 1v2c0 1-1 2-2 2A8 8 0 0 1 0 2c0-1 1-2 2-2z"/></svg>(949)731-2864</div>
        <div class="icon-line"><svg viewBox="0 0 10 10"><path d="M0 2h10v6H0zM0 2l5 3.5L10 2" stroke="#fff" stroke-width=".8"/></svg>info@mwdaccts.example</div>
        <div class="icon-line"><svg viewBox="0 0 10 10"><circle cx="5" cy="5" r="4.5"/><path d="M.5 5h9M5 .5c-2 2.5-2 6.5 0 9M5 .5c2 2.5 2 6.5 0 9" stroke="#fff" stroke-width=".7" fill="none"/></svg>www.mwdaccts.example</div>
      </div>
    </div>
    <div class="letter-body">
      <p>Dear customer,</p>
      <p>Lorem ipsum dolor sit amet, consectetur adipisicing elit, sed do eiusmod tempor incididunt ut labore et dolore magna aliqua. Ut enim ad minim veniam, quis nostrud exercitation ullamco laboris nisi ut aliquip ex ea commodo consequat. Duis aute irure dolor in reprehenderit in voluptate velit esse cillum dolore eu fugiat nulla pariatur. Excepteur sint occaecat cupidatat non proident, sunt in culpa qui officia deserunt mollit anim id est laborum.</p>
      <p>Lorem ipsum dolor sit amet, consectetur adipisicing elit, sed do eiusmod tempor incididunt ut labore et dolore magna aliqua. Ut enim ad minim veniam, quis nostrud exercitation ullamco laboris nisi ut aliquip ex ea commodo consequat. Duis aute irure dolor in reprehenderit in voluptate velit esse cillum dolore eu fugiat nulla pariatur. Excepteur sint occaecat cupidatat non proident, sunt in culpa qui officia deserunt mollit anim id est laborum.</p>
      <p>Lorem ipsum dolor sit amet, consectetur adipisicing elit, sed do eiusmod tempor incididunt ut labore et dolore magna aliqua. Ut enim ad minim veniam, quis nostrud exercitation ullamco laboris nisi ut aliquip ex ea commodo consequat. Duis aute irure dolor in reprehenderit in voluptate velit esse cillum dolore eu fugiat nulla pariatur. Excepteur sint occaecat cupidatat non proident, sunt in culpa qui officia deserunt mollit anim id est laborum.</p>
      <p>Lorem ipsum dolor sit amet, consectetur adipisicing elit, sed do eiusmod tempor incididunt ut labore et dolore magna aliqua. Ut enim ad minim veniam, quis nostrud exercitation ullamco laboris nisi ut aliquip ex ea commodo consequat. Duis aute irure dolor in reprehenderit.</p>
      <p>Yours Sincerely,</p>
      <div class="signature-area" role="img" aria-label="Handwritten signature"></div>
    </div>
    <div class="watermark">Moss Whitfield</div>
    <svg class="accent-stripe" viewBox="0 0 460 12" preserveAspectRatio="none">
      <polygon points="0,0 270,0 282,12 0,12" fill="var(--brand-blue)"/>
      <polygon points="282,9 460,9 460,12 282,12" fill="var(--silver)"/>
    </svg>
  </section>

  <!-- Folder -->
  <section class="sheet folder">
    <div class="firm-name">Moss Whitfield &amp; Danby LLP</div>
    <div class="folder-url">www.mwdaccts.example</div>
  </section>

  <!-- Business card, front -->
  <section class="sheet card card-front">
    <div class="holder-name">DANIEL R. OSTRANDER</div>
    <div class="holder-title">Founder &amp; CEO</div>
    <div class="contact-list">
      <div class="icon-line"><svg viewBox="0 0 10 10"><path d="M2 0h2l1 3-1.5 1a6 6 0 0 0 2.5 2.5L7 5l3 1v2c0 1-1 2-2 2A8 8 0 0 1 0 2c0-1 1-2 2-2z"/></svg>(949)731-2864</div>
      <div class="icon-line"><svg viewBox="0 0 10 10"><path d="M0 2h10v6H0zM0 2l5 3.5L10 2" stroke="#fff" stroke-width=".8"/></svg>info@mwdaccts.example</div>
      <div class="icon-line"><svg viewBox="0 0 10 10"><circle cx="5" cy="5" r="4.5"/><path d="M.5 5h9M5 .5c-2 2.5-2 6.5 0 9M5 .5c2 2.5 2 6.5 0 9" stroke="#fff" stroke-width=".7" fill="none"/></svg>www.mwdaccts.example</div>
    </div>
    <div class="firm-name">Moss Whitfield &amp; Danby LLP</div>
    <div class="rule"></div>
    <div class="address">Moss Whitfield &amp; Danby LLP<br>4827 Larkspur Vale Road,<br>Irvine, CA 92614</div>
    <svg class="accent-stripe" viewBox="0 0 290 12" preserveAspectRatio="none">
      <polygon points="0,4 140,4 148,12 0,12" fill="var(--brand-blue)"/>
      <polygon points="148,10 290,10 290,12 148,12" fill="var(--silver)"/>
    </svg>
  </section>

  <!-- Business card, back -->
  <section class="sheet card card-back">
    <div class="firm-name">Moss Whitfield &amp; Danby LLP</div>
  </section>

  <!-- Envelope -->
  <section class="sheet envelope">
    <div class="firm-name"><span class="mark-square"></span>Moss Whitfield &amp; Danby LLP</div>
    <div class="return-address">Moss Whitfield &amp; Danby LLP<br>4827 Larkspur Vale Road,<br>Irvine, CA 92614</div>
    <div class="watermark">Moss Whitfield</div>
    <svg class="accent-stripe" viewBox="0 0 620 12" preserveAspectRatio="none">
      <polygon points="0,0 330,0 342,12 0,12" fill="var(--brand-blue)"/>
      <polygon points="342,9 620,9 620,12 342,12" fill="var(--silver)"/>
    </svg>
  </section>

</body>
</html>
```